OLU58 biz card & Stationery

LU58 is a personalized shopping experience brought to you, that lets you find and discover fashion goods through a collection of boutiques curated by taste-makers - celebrities, stylists, designers, and fashion bloggers. Boutiques uses visual technology to help fashionistas discover and shop their look and creates the opportunity for designers to showcase their collections and latest inspirations online.

OLU58 is built on technology developed by our team of fashion experts who work with engineers to “teach” our computer systems to understand various patterns, pairings, and genre definitions. When signed into your account, OLU58 learns about your style and preferences and in turn, provides you better results and recommendations over time. Ultimately, OLU58 will provide shoppers with a much richer and interactive shopping experience and help drive traffic to retailers' websites.

We need a definitely cool business card. The card must be black! And must use our official logo which can be download from OLU58.com

The address for Letter head and evenlop, please use 4872 Crestwick Parkway, Sutie 510 Los Angeles CA90412, email will be anyone@OLU58.com, website is www.OLU58.com

thanks

We received some of the design, thanks. But most of the design are not what we want. We need a very clean version with black ground, you may also use some dark gray to add the element. please take a look at http://morvalstudio.no/work/#pelter__ostrama/, we do like this kind of design very much. hope it help.

```html
<!DOCTYPE html>
<html lang="en">
<head>
<meta charset="utf-8">
<title>OLU58 Envelope</title>
<link rel="stylesheet" href="https://fonts.googleapis.com/css2?family=Open+Sans:wght@400&display=swap">
<style>
  :root {
    --backdrop: #6e6e6e;
    --paper: #ffffff;
    --ink: #222222;
    --mark: #1f1f1f;
  }
  html, body {
    margin: 0;
    width: 1200px;
    height: 900px;
    overflow: hidden;
    background: var(--backdrop);
    font-family: "Open Sans", Arial, sans-serif;
  }
  .envelope {
    position: absolute;
    left: 145px;
    top: 238px;
    width: 900px;
    height: 395px;
    background: var(--paper);
    box-shadow: 0 1px 3px rgba(0,0,0,0.35);
  }
  .sender {
    position: absolute;
    left: 41px;
    top: 32px;
  }
  .sender-name {
    display: flex;
    align-items: center;
    gap: 8px;
    margin: 0;
    font-size: 26px;
    font-weight: 400;
    line-height: 34px;
    color: var(--ink);
  }
  .sender-square {
    width: 12px;
    height: 12px;
    background: var(--mark);
  }
  .return-address {
    margin: 18px 0 0;
    font-style: normal;
    font-size: 10.5px;
    line-height: 13px;
    color: var(--ink);
  }
</style>
</head>
<body>
  <div class="envelope">
    <div class="sender">
      <p class="sender-name"><span class="sender-square"></span>OLU58</p>
      <address class="return-address">
        482 Harbor ST Suite 217<br>
        Linden Cove, CA 95418
      </address>
    </div>
  </div>
</body>
</html>
```